Beauty Page

**UPDATED Brief**
We are looking for a website for a beauty organisation that targets both MEN & WOMAN. The focus of the company is in four main areas:

- Health
* Naturopathy & Remedial Massage
- Body
* Yoga
* Personal Training
* Massage
- Skin
* Skin care products such as Velquessa
- Beauty
* Waxing
* Eye Treatments

We have attached the logo, (a sample of the website that I did - based on the book) and the sample of the pdf book
Updates

Dear All,

Thank you for your patience regarding the beauty contest. We were not happy with the designs that were submitted to us. We therefore had the Graphic designer to do the pricelist book to get all the colours for the organisation.

We are now happy to relaunch the contest and invite you all to take a look at the brief, download a sample of the book and the website we designed on what I’m looking for (the website is only a draft so I don’t want you to copy it) and let your creative mind go wild and present some suggestions to us.

Thanks

 

Target Market(s)

Woman & Men age 24 - 60

Industry/Entity Type

It Company

Requirements
Must have
• Use of main colours
Black
White
Gray - (CYMK - 65, 58, 57, 37)
Purpleish - Maroon (CYMK - 52, 69, 47, 25)

Use of the three color dots on the page.
(white, maroon & Gray)
Same fonts as the book
- Helvetica LT Std
Should not have
• Logo must not be altered i.e different colours, fonts, shadows etc...

```html
<!DOCTYPE html>
<html lang="en">
<head>
<meta charset="utf-8">
<title>Serenvale &amp; Beauty</title>
<link rel="stylesheet" href="https://fonts.googleapis.com/css2?family=Arimo:wght@400;700&family=Roboto+Condensed:wght@400&family=Ubuntu:wght@400;700&display=swap">
<style>
:root{
  --maroon:#5c3b65;
  --maroon-dark:#3f2746;
  --maroon-mid:#6e4a78;
  --maroon-light:#8d6d95;
  --gray:#384345;
  --gray-mid:#6b7274;
  --gray-light:#c9cccd;
  --black:#111;
  --white:#fff;
  --line:#dcdcdc;
}
*{margin:0;padding:0;box-sizing:border-box}
html,body{width:1200px;height:1173px;overflow:hidden}
body{
  font-family:"Arimo",Helvetica,sans-serif;color:var(--black);
  background:linear-gradient(180deg,var(--maroon-dark) 0,var(--maroon-light) 220px,var(--maroon-mid) 420px,var(--maroon-dark) 620px,var(--maroon-dark) 100%);
  position:relative;
}
.sheet{position:absolute;left:141px;top:9px;width:918px;height:1032px;background:var(--white);
  border-radius:40% 40% 50% 50%/14px 14px 28px 28px;box-shadow:0 4px 14px rgba(0,0,0,.35)}
.header{position:absolute;left:145px;top:14px;width:910px;height:120px;
  background:linear-gradient(90deg,#e6e7e8 0,#f6f6f6 22%,#fff 45%,#fff 55%,#f6f6f6 78%,#e6e7e8 100%)}
.brand{position:absolute;left:0;right:0;top:30px;text-align:center;font-weight:700;font-size:34px;color:var(--black);letter-spacing:-.5px}
.areas{position:absolute;left:0;right:0;top:80px;display:flex;justify-content:center;align-items:center;gap:10px;font-size:12px;color:var(--gray);letter-spacing:1px}
.dot{width:9px;height:9px;border-radius:50%;display:inline-block}
.dot.white{background:var(--white);border:1px solid var(--gray-light)}
.dot.maroon{background:var(--maroon)}
.dot.gray{background:var(--gray)}
.nav{position:absolute;left:145px;top:134px;width:910px;height:38px;
  background:linear-gradient(180deg,var(--maroon-mid) 0,var(--maroon) 60%,var(--maroon-dark) 100%);border-bottom:3px solid var(--maroon-light);display:flex}
.nav a{font-family:"Ubuntu",sans-serif;font-weight:700;font-size:12px;color:#fff;text-decoration:none;line-height:36px;padding:0 19px;border-right:1px solid var(--maroon-dark)}
.banner{position:absolute;left:147px;top:176px;width:906px;height:255px;overflow:hidden;
  background:linear-gradient(180deg,#fff 0,#f1f1f1 60%,#ddd 100%);border-radius:0 0 50% 50%/0 0 36px 36px}
.banner-photo{position:absolute;left:0;top:0;width:520px;height:100%;
  background:linear-gradient(90deg,#8e9a84 0,#c8cfbf 35%,#ece6e0 70%,rgba(255,255,255,0) 100%)}
.banner-copy{position:absolute;left:549px;top:46px;width:300px;font-family:"Roboto Condensed",sans-serif;color:var(--black)}
.banner-copy h2{font-weight:400;font-size:22px;margin-bottom:6px}
.banner-copy p{font-size:15.5px;line-height:20.5px}
.btn{position:absolute;left:697px;top:352px;width:117px;height:32px;border-radius:4px;
  background:linear-gradient(180deg,var(--maroon-light),var(--maroon-dark));color:#fff;font-family:"Ubuntu",sans-serif;font-weight:700;font-size:17px;text-align:center;line-height:31px;box-shadow:0 2px 3px rgba(0,0,0,.3)}
.arrow{position:absolute;top:393px;width:37px;height:31px;background:var(--maroon);display:flex;align-items:center;justify-content:center}
.arrow.left{left:146px;border-radius:0 0 0 4px}
.arrow.right{left:1017px;border-radius:0 0 4px 0}
.welcome{position:absolute;left:164px;top:472px;width:612px}
.welcome h1{font-family:"Ubuntu",sans-serif;font-weight:400;font-size:23px;color:var(--maroon);margin-bottom:10px}
.welcome p{font-size:11px;line-height:14px}
.welcome strong{color:var(--maroon)}
.card{position:absolute;top:564px;width:295px;height:188px;background:linear-gradient(180deg,#fbfbfb,#efefef);border:1px solid var(--line);border-radius:3px}
.card h3{position:absolute;left:0;right:0;top:20px;text-align:center;font-size:12px;color:var(--maroon);font-weight:700}
.card .media{position:absolute;left:38px;top:38px;width:220px;height:112px}
.video{background:linear-gradient(180deg,#e4e5e6 0,#c9cbcc 45%,#3a3534 60%,#1b1816 100%)}
.video .play{position:absolute;left:92px;top:38px}
.products{background:linear-gradient(180deg,#fff,#eef0f1);border:1px solid #ccc}
.card .more{position:absolute;right:20px;bottom:12px;font-size:10px;color:var(--black)}
.card .more span{text-decoration:underline}
.shave{position:absolute;left:164px;top:797px;width:614px;height:34px;border-radius:4px;
  background:linear-gradient(180deg,var(--maroon-light),var(--maroon) 50%,var(--maroon-dark));color:#fff;font-family:"Ubuntu",sans-serif;font-size:23px;text-align:right;padding-right:19px;line-height:34px}
.shave-shot{position:absolute;left:216px;top:836px;width:150px;height:132px;background:linear-gradient(180deg,#fff,#f0f0f0 50%,var(--gray-light) 85%,#e8e8e8)}
.shave-copy{position:absolute;left:432px;top:869px;width:300px;font-size:11px;line-height:13.7px;color:var(--gray)}
.round{position:absolute;top:884px;width:26px;height:30px;border-radius:50%;background:#f2f2f2;display:flex;align-items:center;justify-content:center}
.shave-rule{position:absolute;left:164px;top:978px;width:614px;height:6px;background:radial-gradient(ellipse at center,#d8d8d8,rgba(255,255,255,0) 70%)}
.side-rule{position:absolute;left:807px;top:462px;width:1px;height:20px;background:var(--line)}
.side-head{position:absolute;left:808px;top:479px;width:227px;height:32px;border-radius:0 4px 4px 0;
  background:linear-gradient(180deg,var(--maroon-mid),var(--maroon));color:#fff;font-family:"Ubuntu",sans-serif;font-weight:700;font-size:12px;line-height:32px;padding-left:12px}
.address{position:absolute;left:820px;top:525px;font-size:11.5px;line-height:13.5px}
.phone{position:absolute;left:820px;top:565px;font-size:11.5px}
.partner{position:absolute;left:808px;width:227px;height:61px;border:1px solid var(--line);border-radius:3px;
  background:linear-gradient(180deg,#fff,#ececec);display:flex;align-items:center;justify-content:center;font-weight:700;font-size:20px;color:var(--gray)}
.like{position:absolute;left:821px;top:824px;display:flex;align-items:center;gap:8px;font-size:10px}
.like b{border:1px solid var(--gray-light);background:#eeeeef;color:var(--gray);padding:3px 8px;border-radius:2px;font-size:10px}
.vip{position:absolute;left:808px;top:864px;width:227px;height:116px;border:1px solid var(--maroon-light);
  background:linear-gradient(180deg,var(--maroon-mid),var(--maroon) 50%,var(--maroon-dark));overflow:hidden;border-radius:2px}
.vip p{position:absolute;left:21px;top:34px;color:#fff;font-family:"Ubuntu",sans-serif;font-weight:700;font-size:14px;line-height:14px}
.vip p .big{font-size:23px;line-height:24px}
.ribbon{position:absolute;left:947px;top:897px}
.footer{position:absolute;left:0;right:0;top:1085px;text-align:center;font-size:12px;color:#d3c3d7}
.footer a{color:#d3c3d7;text-decoration:none;padding:0 12px}
.copy{position:absolute;left:0;right:0;top:1116px;text-align:center;font-size:12px;color:#b19fb6}
</style>
</head>
<body>
<div class="sheet"></div>
<header class="header" role="img" aria-label="Soft floral ornament border">
  <div class="brand">Serenvale &amp; Beauty</div>
  <div class="areas"><span class="dot white"></span>HEALTH<span class="dot maroon"></span>BODY<span class="dot gray"></span>SKIN<span class="dot white"></span>BEAUTY</div>
</header>
<nav class="nav">
  <a href="#">Home</a><a href="#">About Us</a><a href="#">Services &amp; Treatments</a><a href="#">Contact Us</a>
</nav>
<section class="banner">
  <div class="banner-photo" role="img" aria-label="Spa photo of a relaxed client with bamboo leaves"></div>
  <div class="banner-copy">
    <h2>Lorem Ipsum is simply dummy!</h2>
    <p>Lorem Ipsum is simply dummy text of the printing and typesetting industry. Lorem Ipsum has been the industry's standard dummy text ever since the 1500s</p>
  </div>
</section>
<div class="btn">Know More</div>
<div class="arrow left"><svg width="14" height="16" viewBox="0 0 14 16"><path d="M10 2 4 8l6 6" fill="none" stroke="#fff" stroke-width="3"/></svg></div>
<div class="arrow right"><svg width="14" height="16" viewBox="0 0 14 16"><path d="M4 2l6 6-6 6" fill="none" stroke="#fff" stroke-width="3"/></svg></div>

<section class="welcome">
  <h1>Welcome</h1>
  <p><strong>Serenvale &amp; Beauty</strong> is a health, massage skincare centre that provides quality treatments and education to each and every client to cater for all individuals.</p>
</section>

<article class="card" style="left:164px">
  <h3>REVOLUTIONARY NEW TREATMENTS</h3>
  <div class="media video" role="img" aria-label="Video still of a treatment device on a stage">
    <svg class="play" width="36" height="36" viewBox="0 0 36 36"><circle cx="18" cy="18" r="17" fill="#ddd" stroke="#888"/><path d="M14 11l11 7-11 7z" fill="#222"/></svg>
  </div>
  <div class="more">&#9670; <span>Watch Videos</span></div>
</article>
<article class="card" style="left:486px">
  <h3>New Arrival from Maré Lune</h3>
  <div class="media products" role="img" aria-label="Skin care tubes and jars"></div>
  <div class="more">&#9670; <span>know more</span></div>
</article>

<div class="shave">Shave</div>
<div class="shave-shot" role="img" aria-label="Shave kit tubes"></div>
<p class="shave-copy">Guarantee a confident look with the Velquessa Shave system Kit. it contains products to prepare the skin for shaving by softening the hair and opening the pores. protecting the skin during shaving and calming the skin and minimizing bumps and razor burn after shaving.</p>
<div class="round" style="left:158px"><svg width="12" height="14"><path d="M9 2 3 7l6 5" fill="none" stroke="#666" stroke-width="2.5"/></svg></div>
<div class="round" style="left:755px"><svg width="12" height="14"><path d="M3 2l6 5-6 5" fill="none" stroke="#666" stroke-width="2.5"/></svg></div>
<div class="shave-rule"></div>

<div class="side-rule"></div>
<div class="side-head">Contact Information</div>
<p class="address">Unit 4 / 72 Harlow Road<br>ELMSFIELD, WA 6099</p>
<p class="phone"><b>Phone:</b> (08) 5550 1427</p>
<div class="partner" style="top:591px">Velquessa</div>
<div class="partner" style="top:667px">Verdan Peel</div>
<div class="partner" style="top:743px">Silverring</div>
<div class="like"><b>Like</b><span>563 people like this.</span></div>
<div class="vip"><p>JOIN OUR VIP CLUB AND<br>EARN DISCOUNTS ON<br><span class="big">PRODUCTS</span></p></div>
<svg class="ribbon" width="92" height="90" viewBox="0 0 92 90">
  <path d="M92 0v50L50 90H4z" fill="var(--gray)"/>
  <path d="M4 90h46l-4-4z" fill="var(--black)"/>
  <text x="62" y="66" transform="rotate(-45 62 66)" fill="#fff" font-family="Ubuntu, sans-serif" font-weight="700" font-size="11" text-anchor="middle">LEARN</text>
  <text x="70" y="76" transform="rotate(-45 70 76)" fill="#fff" font-family="Ubuntu, sans-serif" font-weight="700" font-size="11" text-anchor="middle">MORE</text>
</svg>

<footer class="footer">
  <a href="#">Home</a>|<a href="#">About Us</a>|<a href="#">Services &amp; Treatments</a>|<a href="#">Contact Us</a>
</footer>
<p class="copy">© 2009 Serenvale &amp; Beauty. All Rights Reserved.</p>
</body>
</html>
```